Music Industry Business Needs a Business Card Design

Copper Lantern is an audio mastering company that has been in business for 20 years. Mastering is the final creative step in the music production chain. Our job is to make the music sound as good as it possibly can prior to release to the public. Our world is technical, artistic, precise. We work on everything from independent artists to the music for the Grandfield Cup. We are looking for a new, more modern business card design. I am uploading a copy of our logo, although it doesn't absolutely need to be included in the design.

Target Market(s)

Music Industry Professionals

Industry/Entity Type

Business

Contact Information for Business Card

Address, Phone, Email, Website, Name, Job Title

Font styles to use
Sans Serif

Requirements
Must have
• Sorry, but I don't have any concrete things to request. If I had a clear idea of what I want, I would probably just design something myself. I am looking for fresh input and thought I would try this.
Should not have
• Anything that is typical, such as headphones or the like.

```html
<!DOCTYPE html>
<html lang="en">
<head>
<meta charset="utf-8">
<title>Copper Lantern – Business Card</title>
<link rel="stylesheet" href="https://fonts.googleapis.com/css2?family=Arimo:wght@400;700&display=swap">
<style>
  :root {
    --backdrop: #d6d7da;
    --card-white: #ffffff;
    --wave-edge: #2a50a8;
    --wave-navy: #1f3c6e;
    --wave-deep: #1a3360;
    --pill: #2d58b4;
    --ink-light: #ffffff;
    --ink-dark: #1d1f24;
  }
  html, body {
    margin: 0;
    width: 1200px;
    height: 900px;
    overflow: hidden;
    background: var(--backdrop);
    font-family: "Arimo", Arial, sans-serif;
  }
  .stage {
    width: 1200px;
    height: 900px;
    display: flex;
    align-items: center;
    justify-content: center;
  }
  .business-card {
    width: 400px;
    height: 700px;
    display: block;
    filter: drop-shadow(0 6px 14px rgba(0,0,0,0.22));
  }
  .card-base { fill: var(--card-white); }
  .wave-edge { fill: var(--wave-edge); }
  .wave-body { fill: url(#waveShade); }
  .brand-name {
    font-family: "Arimo", Arial, sans-serif;
    font-weight: 400;
    font-size: 19px;
    letter-spacing: 2px;
    fill: var(--ink-dark);
  }
  .brand-dot { fill: none; stroke: var(--ink-dark); stroke-width: 1.4; }
  .person-name {
    font-family: "Arimo", Arial, sans-serif;
    font-weight: 400;
    font-size: 30px;
    fill: var(--ink-light);
  }
  .person-role {
    font-family: "Arimo", Arial, sans-serif;
    font-size: 14px;
    fill: var(--ink-light);
    opacity: 0.85;
  }
  .contact-pill { fill: var(--pill); }
  .contact-text {
    font-family: "Arimo", Arial, sans-serif;
    font-size: 15px;
    fill: var(--ink-light);
  }
  .contact-icon { fill: var(--ink-light); }
  .contact-icon-line { fill: none; stroke: var(--ink-light); stroke-width: 1.4; }
</style>
</head>
<body>
<main class="stage">
  <svg class="business-card" viewBox="0 0 400 700" xmlns="http://www.w3.org/2000/svg" aria-label="Copper Lantern business card">
    <defs>
      <radialGradient id="waveShade" cx="0.55" cy="0.5" r="0.6">
        <stop offset="0" stop-color="#1a3360"/>
        <stop offset="1" stop-color="#223f74"/>
      </radialGradient>
      <clipPath id="cardClip"><rect width="400" height="700"/></clipPath>
    </defs>

    <g clip-path="url(#cardClip)">
      <rect class="card-base" width="400" height="700"/>

      <path class="wave-edge" d="M0,0 H185 C240,140 320,275 400,300 V700 H228 C168,560 80,450 0,432 Z"/>
      <path class="wave-body" d="M0,0 H165 C222,150 305,292 400,320 V700 H256 C196,555 100,430 0,410 Z"/>

      <g class="brand">
        <circle class="brand-dot" cx="318" cy="56" r="9"/>
        <text class="brand-name" x="318" y="100" text-anchor="middle">COPPER</text>
        <text class="brand-name" x="318" y="126" text-anchor="middle">LANTERN</text>
      </g>

      <text class="person-name" x="34" y="172">Elena Marsh</text>
      <text class="person-role" x="36" y="194">Director</text>

      <g class="contact-list">
        <rect class="contact-pill" x="-20" y="214" width="200" height="28" rx="14"/>
        <path class="contact-icon" d="M30,221 q-3,0 -3,4 q1,8 9,11 q3,0 4,-3 l-3,-3 l-2,2 q-4,-2 -5,-5 l2,-2 z"/>
        <text class="contact-text" x="52" y="233">0161 555 0142</text>

        <rect class="contact-pill" x="-20" y="252" width="200" height="28" rx="14"/>
        <rect class="contact-icon-line" x="28" y="258" width="8" height="15" rx="1.5"/>
        <text class="contact-text" x="52" y="271">0161 555 0198</text>

        <rect class="contact-pill" x="-20" y="290" width="265" height="28" rx="14"/>
        <rect class="contact-icon-line" x="25" y="298" width="14" height="10"/>
        <path class="contact-icon-line" d="M25,298 l7,6 l7,-6"/>
        <text class="contact-text" x="52" y="309">info@copperlantern.com</text>

        <rect class="contact-pill" x="-20" y="328" width="260" height="28" rx="14"/>
        <circle class="contact-icon-line" cx="32" cy="342" r="7"/>
        <path class="contact-icon-line" d="M25,342 h14 M32,335 q-4,7 0,14 M32,335 q4,7 0,14"/>
        <text class="contact-text" x="52" y="347">www.copperlantern.com</text>

        <rect class="contact-pill" x="-20" y="366" width="280" height="28" rx="14"/>
        <path class="contact-icon" d="M32,387 q-7,-8 -7,-12 a7,7 0 0 1 14,0 q0,4 -7,12 z"/>
        <circle cx="32" cy="375" r="2.4" fill="#2d58b4"/>
        <text class="contact-text" x="52" y="385">48 Harbor Lane, Millbrook</text>
      </g>
    </g>
  </svg>
</main>
</body>
</html>
```